Informational Site for Advanced Chemistry R&D

The company develops oxidation chemistry for air, water, fuel pollution controls. The site has been prototyped at www.velkorlabs.net. Take a look. Now, the task is to design it for eye-catching beauty with use of color, on-page scroll-driven color transition and parallax effects. Should capture the themes: high technology, wow it's beautiful, modern, uncluttered, clean urban environment.

Target Market(s)

China Environmentally Conscious Government and Industry,

Industry/Entity Type

It Company

Number of Pages Required

3 page

Font styles to use
Sans Serif

Requirements
Must have
• Parallax effects, desktop compatible, Rich, Modern, Simple, Graphic
Nice to have
• Mobile Phone Compatible
Should not have
• Flash, or anything that is slow to load or requires high bandwidth

```html
<!DOCTYPE html>
<html lang="en">
<head>
<meta charset="utf-8">
<title>Velkor Labs – Advanced Oxidation Science</title>
<link rel="stylesheet" href="https://fonts.googleapis.com/css2?family=Open+Sans:wght@400;600;700;800&family=Oswald:wght@500;600&display=swap">
<style>
:root{
  --teal:#2bb1a6;
  --blue:#1f7fc3;
  --footer:#1b6fb4;
  --footer-dark:#175e9b;
  --orange:#f4a422;
  --rust:#d9622b;
  --lime:#8cbc2b;
  --ink:#333a40;
  --muted:#7a8590;
  --light:#f2f4f6;
  --white:#ffffff;
}
*{box-sizing:border-box;margin:0;padding:0}
html,body{width:1200px;height:3956px;overflow:hidden}
body{position:relative;font-family:"Open Sans",Arial,sans-serif;color:var(--ink);background:var(--white)}
.abs{position:absolute}

/* hero */
.hero{left:0;top:0;width:1200px;height:672px;
  clip-path:polygon(0 0,1200px 0,1200px 600px,600px 672px,0 600px);
  background:linear-gradient(180deg,#2b3138 0%,#4d5560 30%,#8a949c 52%,#6c8a54 66%,#5a8a2e 80%,#3f6f1f 100%)}
.logo{left:56px;top:26px;display:flex;align-items:center;gap:10px;color:var(--white);font-weight:700;font-size:20px}
.logo-dot{width:26px;height:26px;border-radius:50%;background:var(--teal)}
.main-nav{right:40px;top:44px;display:flex;gap:46px}
.main-nav a{color:var(--white);text-decoration:none;font-weight:700;font-size:15px;letter-spacing:1px}
.hero-title{left:0;width:1200px;top:336px;text-align:center;color:var(--white);font-weight:700;font-size:44px;letter-spacing:8px}
.hero-sub{left:0;width:1200px;top:398px;text-align:center;color:var(--white);font-size:24px;letter-spacing:3px}
.hero-arrow{top:378px}
.hero-down{left:582px;top:618px}

/* intro row */
.tile{top:812px;height:256px;color:var(--white);padding:24px 26px}
.tile h3{font-size:26px;font-weight:600;display:flex;align-items:center;gap:10px;margin-bottom:18px}
.tile h3 span{width:18px;height:18px;border:2px solid var(--white);border-radius:3px}
.tile p{font-size:13px;line-height:19px}
.tile .date{font-size:12px;opacity:.9;margin:4px 0}
.tile .more{position:absolute;right:18px;bottom:14px;background:rgba(0,0,0,.25);font-size:11px;padding:3px 10px}
.tile .dots{position:absolute;left:50%;bottom:16px;display:flex;gap:6px;transform:translateX(-50%)}
.tile .dots i{width:7px;height:7px;border-radius:50%;background:rgba(255,255,255,.5)}
.tile .dots i:first-child{background:var(--white)}
.tile-events{left:72px;width:288px;background:var(--teal)}
.tile-news{left:836px;width:292px;background:var(--blue)}
.mission{left:380px;top:812px;width:440px;height:256px;text-align:center;padding-top:18px}
.mission h2{font-family:"Oswald",sans-serif;font-weight:600;font-size:22px;line-height:26px;color:var(--ink);letter-spacing:.3px}
.mission-mark{margin:20px auto 6px;display:flex;align-items:center;justify-content:center;gap:10px;font-weight:700;font-size:24px;color:var(--blue)}
.mission-mark i{width:30px;height:30px;border-radius:50%;background:var(--teal)}
.mission .btn-line{display:inline-block;margin-top:18px;border:1px solid #cfd5da;padding:9px 18px;font-size:12px;font-weight:600;color:var(--ink);text-transform:uppercase}

.section-title{left:0;width:1200px;text-align:center;font-weight:700;font-size:34px;color:var(--ink)}
.section-title::after{content:"";display:block;width:70px;height:4px;background:var(--teal);margin:14px auto 0}

/* solutions */
.solution{left:0;width:1200px;height:444px}
.sol-water{top:1252px;background:linear-gradient(180deg,#2d6fb6 0%,#5c97cf 35%,#9cb8c4 55%,#5f6f63 75%,#2f4a5e 100%)}
.sol-diesel{top:1696px;background:linear-gradient(160deg,#2f6fb0 0%,#6ea0cf 35%,#d8d2c0 60%,#a8a08c 100%)}
.sol-coal{top:2140px;background:linear-gradient(180deg,#3d80c4 0%,#79aede 40%,#6b7152 70%,#4f5a3c 100%)}
.sol-voc{top:2584px;height:444px;background:linear-gradient(180deg,#6a7e92 0%,#a9b8c4 45%,#d7dde1 75%,#eef1f2 100%)}
.sol-card{width:296px;padding:22px 22px;color:var(--white)}
.sol-card h3{font-size:34px;font-weight:800;line-height:38px;text-transform:uppercase;margin-bottom:10px}
.sol-card p{font-size:13px;line-height:19px}
.sol-card .btn-ghost{display:inline-block;margin-top:18px;border:1px solid var(--white);font-size:11px;font-weight:600;padding:8px 12px;text-transform:uppercase}
.card-water{left:40px;top:1392px;background:var(--orange)}
.card-diesel{left:868px;top:1740px;background:var(--teal)}
.card-coal{left:40px;top:2180px;background:var(--rust)}
.card-voc{left:868px;top:2736px;background:var(--lime)}

/* posts */
.post{top:3188px;width:334px}
.post-img{height:264px}
.post h4{font-size:15px;font-weight:600;line-height:20px;margin-top:24px;color:var(--ink)}
.post .meta{font-size:12px;color:var(--teal);margin-top:10px}
.post-1{left:72px}.post-1 .post-img{background:linear-gradient(180deg,#56b7c9,#3f9bb0 60%,#2f7f92)}
.post-2{left:434px}.post-2 .post-img{background:linear-gradient(180deg,#3f8fe0,#8cc5f0 45%,#9ccb4a 70%,#5f9a23)}
.post-3{left:794px}.post-3 .post-img{background:linear-gradient(180deg,#9fb0bb,#6f8592 50%,#2d4a66)}

/* footer */
.site-footer{left:0;top:3580px;width:1200px;height:376px;background:var(--footer);color:var(--white)}
.f-col{top:52px}
.f-col h5{font-size:15px;font-weight:700;text-transform:uppercase;margin-bottom:16px}
.f-col p,.f-col li{font-size:13px;line-height:22px;list-style:none;opacity:.9}
.f-links{display:grid;grid-template-columns:90px 90px}
.social{display:flex;gap:8px;margin-top:10px}
.social i{width:26px;height:26px;border-radius:50%;border:1px solid rgba(255,255,255,.7)}
.subscribe{display:flex;margin-top:14px;width:260px;height:34px}
.subscribe span{flex:1;background:var(--white);color:#99a2aa;font-size:12px;padding:8px 12px;border-radius:17px 0 0 17px}
.subscribe b{width:44px;background:var(--teal);border-radius:0 17px 17px 0;display:flex;align-items:center;justify-content:center}
.f-bottom{left:0;bottom:0;width:1200px;height:56px;background:var(--footer-dark);font-size:12px;padding:20px 72px;opacity:.95}
</style>
</head>
<body>

<header class="hero abs" role="img" aria-label="Storm clouds over a bright green field"></header>
<div class="logo abs"><i class="logo-dot"></i>Velkor Labs</div>
<nav class="main-nav abs">
  <a href="#">HOME</a><a href="#">WATER</a><a href="#">DIESEL</a><a href="#">COAL</a><a href="#">VOC</a><a href="#">ABOUT</a>
</nav>
<h1 class="hero-title abs">ADVANCED OXIDATION SCIENCE</h1>
<p class="hero-sub abs">FOR ENVIRONMENTAL POLLUTION MANAGEMENT</p>
<svg class="hero-arrow abs" style="left:28px" width="24" height="40" viewBox="0 0 24 40"><path d="M20 4 4 20l16 16" fill="none" stroke="#fff" stroke-width="4"/></svg>
<svg class="hero-arrow abs" style="right:28px" width="24" height="40" viewBox="0 0 24 40"><path d="M4 4l16 16L4 36" fill="none" stroke="#fff" stroke-width="4"/></svg>
<svg class="hero-down abs" width="36" height="36" viewBox="0 0 36 36"><circle cx="18" cy="18" r="16" fill="none" stroke="#fff" stroke-width="2"/><path d="M11 15l7 7 7-7" fill="none" stroke="#fff" stroke-width="2"/></svg>

<section class="tile tile-events abs">
  <h3><span></span>Events</h3>
  <p><b>Pilot reactor trial begins</b></p>
  <p class="date">07 Jan 2016</p>
  <p>Field results show strong removal of organic load in plant water.</p>
  <div class="dots"><i></i><i></i><i></i></div>
  <span class="more">More</span>
</section>

<section class="mission abs">
  <h2>ENVIRONMENTAL POLLUTION CONTROL SOLUTIONS<br>EMPLOYING NATURE'S MOST REACTIVE FREE RADICAL</h2>
  <div class="mission-mark"><i></i>Velkor Labs</div>
  <span class="btn-line">Learn about advanced oxidation chemistry</span>
</section>

<section class="tile tile-news abs">
  <h3><span></span>News</h3>
  <p><b>Partner lab joins research</b></p>
  <p class="date">07 Jan 2016</p>
  <p>Our team shares new data on radical chemistry for fuel treatment.</p>
  <div class="dots"><i></i><i></i><i></i></div>
  <span class="more">More</span>
</section>

<h2 class="section-title abs" style="top:1156px">SOLUTIONS FOR</h2>

<div class="solution sol-water abs" role="img" aria-label="Circular wastewater treatment basin with spraying arms"></div>
<article class="sol-card card-water abs">
  <h3>Wastewater</h3>
  <p>Hydroxyl radical treatment breaks down stubborn organics in municipal and industrial water streams, leaving clean discharge with no added chemical residue or sludge to manage.</p>
  <span class="btn-ghost">Learn more</span>
</article>

<div class="solution sol-diesel abs" role="img" aria-label="Large white fuel storage tanks with stairways against a blue sky"></div>
<article class="sol-card card-diesel abs">
  <h3>Diesel Fuel</h3>
  <p>Oxidative desulfurization lowers sulfur in diesel fuel at mild temperature and pressure, giving refiners a cleaner product with lower cost and a smaller plant footprint.</p>
  <span class="btn-ghost">Learn more</span>
</article>

<div class="solution sol-coal abs" role="img" aria-label="Power plant cooling towers under a blue sky"></div>
<article class="sol-card card-coal abs">
  <h3>Coal Flue Gas</h3>
  <p>Gas phase oxidation captures sulfur and nitrogen oxides from coal flue gas in one step, turning emissions into useful fertilizer salts for local farms.</p>
  <span class="btn-ghost">Learn more</span>
</article>

<div class="solution sol-voc abs" role="img" aria-label="Industrial smokestacks releasing white smoke"></div>
<article class="sol-card card-voc abs">
  <h3>Volatile<br>Organics</h3>
  <p>Radical driven oxidation destroys volatile organic compounds in exhaust air from printing, coating and chemical plants, for cleaner skies over growing cities.</p>
  <span class="btn-ghost">Learn more</span>
</article>

<h2 class="section-title abs" style="top:3070px">LATEST POSTS</h2>

<article class="post post-1 abs">
  <div class="post-img" role="img" aria-label="Cooling towers in a teal tinted haze"></div>
  <h4>New reactor design lowers energy use for city water treatment plants</h4>
  <p class="meta">Lin Wei | on 11th January, 2016</p>
</article>
<article class="post post-2 abs">
  <div class="post-img" role="img" aria-label="Sunlit green meadow under a blue sky"></div>
  <h4>Clean air study shows sharp drop in urban ozone levels this spring</h4>
  <p class="meta">Lin Wei | on 11th January, 2016</p>
</article>
<article class="post post-3 abs">
  <div class="post-img" role="img" aria-label="Engineers in hard hats reviewing an industrial site"></div>
  <h4>Engineers test compact oxidation unit at coastal refinery site</h4>
  <p class="meta">Lin Wei | on 11th January, 2016</p>
</article>

<footer class="site-footer abs">
  <div class="f-col abs" style="left:72px">
    <h5>Company</h5>
    <ul class="f-links"><li>HOME</li><li>COAL</li><li>WATER</li><li>VOC</li><li>DIESEL</li><li>ABOUT</li></ul>
  </div>
  <div class="f-col abs" style="left:340px">
    <h5>Come and visit</h5>
    <p>Velkor Labs Ltd.<br>88 Harbor Road<br>Ningbo, China</p>
    <p style="margin-top:12px">View on map</p>
  </div>
  <div class="f-col abs" style="left:600px">
    <h5>Get in touch</h5>
    <p>1-800-000-0000<br>info@velkorlabs.net</p>
    <div class="social"><i></i><i></i></div>
  </div>
  <div class="f-col abs" style="left:868px">
    <h5>Stay informed</h5>
    <p>Get news, notes, insights and events</p>
    <div class="subscribe"><span>Email address</span><b><svg width="14" height="14" viewBox="0 0 14 14"><path d="M4 2l5 5-5 5" fill="none" stroke="#fff" stroke-width="2"/></svg></b></div>
  </div>
  <div class="f-bottom abs">© 2016 Velkor Labs. All rights reserved.</div>
</footer>

</body>
</html>
```